Web Page Design for a Website that Provides Tutoring

I am looking to create an online tutoring website. The website will allow parents or students to contact tutors with a view to instructing them to tutor themselves or their children.

The name of the website is LendYourLessons.

This brief is to create the design for one of the web pages for this web site. I am hoping the same designer will be available to design other pages.

The page I want designed is one of the more complex and I have attached the design as an excel spreadsheet. The web page needs to include all the items on this page but if you want to change the positioning of the items then Im fine with that.

I recently had two logos created for this website. My favourite is the one with a mortar board but im not sure I like the colours. I have attached both of these logos and you can use either of them, change the colours or create something different. I just want a design pleasing to the eye. If the logo is changed I would like that in a seperate file.

So can you please submit designs for this page. I have attached the two logos which you can use, change or if you feel you have a better idea then you can use that.

On the spreadsheet the Send Message, Favourite etc are buttons.

Target Market(s)

People who want to better themselves.
Possible middle class to upper class.

Industry/Entity Type

Tutoring

Number of Pages Required

1 page

Requirements
Must have
• The designs must have alot of the information attached in the spreadsheet.

```html
<!DOCTYPE html>
<html lang="en">
<head>
<meta charset="utf-8">
<title>LendYourLessons – Home</title>
<link rel="stylesheet" href="https://fonts.googleapis.com/css2?family=Open+Sans:ital,wght@0,400;0,600;0,700;0,800;1,400;1,600;1,700&display=swap">
<style>
:root{
  --navy:#0f2c57;
  --navy-deep:#0b2247;
  --navy-top:#2c4b80;
  --field:#17417c;
  --orange:#fb6a45;
  --yellow:#f7b51c;
  --green:#2f5b22;
  --star:#2a6fd6;
  --text:#555;
  --dark:#1d1d1d;
  --footer:#1a1a1a;
  --footer-low:#111;
  --white:#fff;
}
*{box-sizing:border-box;margin:0;padding:0}
html,body{width:1200px;height:3309px;overflow:hidden}
body{font-family:"Open Sans",Arial,sans-serif;color:var(--text);background:var(--white);position:relative}
.abs{position:absolute}

/* header */
.topbar{left:0;top:0;width:1200px;height:40px;background:var(--navy-top);color:#dfe6f3;font-size:11px}
.topbar .info{position:absolute;top:13px;display:flex;align-items:center;gap:6px}
.topbar .sep{position:absolute;top:10px;width:1px;height:20px;background:#6c84ad}
.navbar{left:0;top:40px;width:1200px;height:92px;background:var(--navy-deep)}
.brand-tab{left:90px;top:26px;width:210px;height:106px;background:#112b55;clip-path:polygon(10% 0,90% 0,100% 100%,0 100%)}
.brand{left:100px;top:96px;width:200px;text-align:center;color:var(--white);font-weight:700;font-size:19px;display:flex;align-items:center;justify-content:center;gap:8px}
.brand .mark{width:14px;height:14px;background:var(--orange)}
.nav{left:404px;top:82px;display:flex;gap:0;color:var(--white);font-size:14px;font-weight:600}
.nav span{position:absolute;white-space:nowrap}

/* hero */
.hero{left:0;top:132px;width:1200px;height:607px;background:linear-gradient(100deg,#8d9bb6 0%,#a9a9b8 35%,#c0b3a7 55%,#8e9fb8 100%)}
.hero-shade{left:0;top:132px;width:1200px;height:607px;background:rgba(48,70,120,.45)}
.hero h1{left:0;top:372px;width:1200px;text-align:center;color:var(--white);font-size:62px;font-weight:800;letter-spacing:1px}
.hero-sub{left:200px;top:448px;width:800px;text-align:center;color:var(--white);font-style:italic;font-weight:600;font-size:16px;line-height:28px}
.btn{display:flex;align-items:center;justify-content:center;font-size:13px;font-weight:600;color:var(--white)}
.btn-send{left:413px;top:532px;width:172px;height:39px;background:var(--orange)}
.btn-view{left:613px;top:532px;width:172px;height:39px;border:1.5px solid var(--white)}

/* section headings */
.heading{font-size:28px;font-weight:600;color:var(--green);white-space:nowrap}
.heading .lead{color:var(--navy)}
.heading-rule{height:2px;background:var(--orange);width:105px}
.subhead{font-size:14px;font-style:italic;font-weight:600;color:var(--dark)}

/* welcome */
.welcome-text{left:84px;top:913px;width:1030px;font-size:14.5px;line-height:26px;color:#666}
.stat-card{left:84px;top:1013px;width:337px;height:112px;background:var(--orange)}
.stat-title{font-size:20px;font-style:italic;font-weight:600;color:var(--orange)}
.divider{width:4px;height:112px;background:var(--orange)}
.stars{display:flex;gap:3px}

/* subjects / signup */
.subjects{left:0;top:1209px;width:600px;height:468px;background:linear-gradient(135deg,#2e4a7c,#23406f 60%,#1c3764)}
.signup{left:600px;top:1209px;width:600px;height:468px;background:var(--navy)}
.table{left:84px;top:1394px;width:516px;font-size:15px;color:var(--white)}
.table .row{position:relative;height:38px;margin-bottom:2px;background:rgba(255,255,255,.12)}
.table .row.head{background:none;color:var(--orange);font-size:13px;font-weight:600}
.table .row span{position:absolute;top:9px}
.note{left:84px;top:1530px;width:450px;color:var(--white);font-size:15px;line-height:26px}
.field{left:717px;width:397px;height:44px;background:var(--field);color:#9fb2d3;font-size:13px;padding:13px 18px}
.btn-quote{left:717px;top:1538px;width:176px;height:37px;background:var(--yellow);color:var(--dark);font-size:12px;font-weight:700}

/* courses */
.course-img{top:1868px;width:242px;height:184px}
.course-title{top:2064px;font-size:15px;font-weight:600;color:var(--dark)}
.course-meta{top:2094px;width:242px;font-size:12px;color:#999;display:flex;align-items:center;gap:8px}
.course-meta .price{color:var(--orange);font-style:italic;font-weight:600;margin-left:20px}

/* counters */
.counters{left:0;top:2195px;width:1200px;height:154px;background:var(--orange)}
.count{top:2220px;color:var(--white);font-size:82px;font-weight:400;line-height:100px}
.count-label{top:2260px;color:var(--white);font-size:14px;font-weight:600;line-height:19px;text-transform:uppercase}

/* news */
.news-img{top:2563px;height:172px}
.news-date{width:52px;height:56px;background:var(--yellow);color:var(--white);font-weight:700;font-size:16px;line-height:21px;text-align:center;padding-top:6px}
.news-meta{top:2747px;font-size:13px;font-style:italic;color:#888;white-space:nowrap}
.news-meta b{font-weight:400;margin-left:38px}
.news-title{top:2774px;width:320px;font-size:15px;font-weight:600;color:var(--dark);line-height:20px}
.news-text{top:2818px;width:320px;font-size:13px;color:#777;line-height:19px}

/* footer */
.footer{left:0;top:2956px;width:1200px;height:302px;background:var(--footer)}
.footer-low{left:0;top:3258px;width:1200px;height:51px;background:var(--footer-low);color:#999;font-size:12px;text-align:center;line-height:51px}
.foot-brand{left:84px;top:3076px;color:var(--white);font-size:19px;font-weight:700;display:flex;align-items:center;gap:8px}
.foot-brand .mark{width:14px;height:14px;background:var(--orange)}
.foot-about{left:84px;top:3115px;width:290px;color:#ccc;font-size:13px;line-height:20px}
.social{top:3188px;width:32px;height:32px;background:#555}
.foot-head{top:3030px;color:var(--white);font-size:14px;font-style:italic;font-weight:600}
.foot-rule{top:3054px;width:105px;height:2px;background:var(--yellow)}
.foot-list{top:3068px;color:#bbb;font-size:12.5px;line-height:22px;list-style:none}
.contact-row{left:860px;width:260px;color:#ccc;font-size:12.5px;line-height:19px}
</style>
</head>
<body>

<!-- header -->
<div class="abs topbar">
  <div class="info" style="left:630px">
    <svg width="12" height="12" viewBox="0 0 12 12"><circle cx="6" cy="6" r="5" fill="none" stroke="#fb6a45" stroke-width="1.5"/><path d="M6 3v3l2 1" stroke="#fb6a45" stroke-width="1.4" fill="none"/></svg>
    <span>MON - FRI : 9:00AM - 06:00PM</span>
  </div>
  <div class="sep" style="left:836px"></div>
  <div class="info" style="left:850px">
    <svg width="12" height="12" viewBox="0 0 12 12"><path d="M2 1l2.5 0 1 3-1.5 1a7 7 0 0 0 3 3l1-1.5 3 1V10a1.5 1.5 0 0 1-1.5 1.5A9.5 9.5 0 0 1 .5 2.5 1.5 1.5 0 0 1 2 1z" fill="#fb6a45"/></svg>
    <span>+1-555-014-2290</span>
  </div>
  <div class="sep" style="left:976px"></div>
  <div class="info" style="left:990px">
    <svg width="11" height="12" viewBox="0 0 11 12"><rect x="1" y="5" width="9" height="7" rx="1" fill="#fb6a45"/><path d="M3 5V3.5a2.5 2.5 0 0 1 5 0V5" stroke="#fb6a45" stroke-width="1.4" fill="none"/></svg>
    <span>Register &nbsp;|&nbsp; Login</span>
  </div>
</div>
<div class="abs navbar"></div>
<div class="abs brand-tab"></div>
<div class="abs brand"><span class="mark"></span>LendYourLessons</div>
<nav class="abs nav" aria-label="Main">
  <span style="left:0">HOME</span>
  <span style="left:77px">SEARCH</span>
  <span style="left:167px">STUDENT</span>
  <span style="left:269px">TUTOR</span>
  <span style="left:350px">ABOUT</span>
  <span style="left:439px">CONTACT</span>
</nav>
<svg class="abs" style="left:1087px;top:74px" width="26" height="26" viewBox="0 0 26 26"><circle cx="10" cy="10" r="7.5" fill="none" stroke="#fff" stroke-width="2.5"/><path d="M15.5 15.5l7 7" stroke="#fff" stroke-width="3" stroke-linecap="round"/></svg>

<!-- hero -->
<div class="abs hero" role="img" aria-label="Photo of a tutor helping a young boy with his lesson at a desk"></div>
<div class="abs hero-shade"></div>
<svg class="abs" style="left:62px;top:413px" width="24" height="44" viewBox="0 0 24 44"><path d="M20 2L4 22l16 20" fill="none" stroke="#fff" stroke-width="2"/></svg>
<svg class="abs" style="left:1114px;top:413px" width="24" height="44" viewBox="0 0 24 44"><path d="M4 2l16 20L4 42" fill="none" stroke="#fff" stroke-width="2"/></svg>
<h1 class="abs hero h1" style="left:0;top:372px;width:1200px;height:auto;background:none;text-align:center;color:#fff;font-size:62px;font-weight:800;letter-spacing:1px">LEND YOUR LESSONS</h1>
<p class="abs hero-sub">Lorem ipsum dolor sit amet, consectetur adipiscing elit. Phasellus molestie lorem vitae velit con sect tur malesuada. Phasellus velit mauris, commodo at tincidunt et</p>
<div class="abs btn btn-send">Send Message</div>
<div class="abs btn btn-view">View Service</div>

<!-- welcome -->
<h2 class="abs heading" style="left:84px;top:830px"><span class="lead">Wel</span>come To Lend Your Lessons</h2>
<div class="abs heading-rule" style="left:515px;top:858px"></div>
<p class="abs subhead" style="left:84px;top:869px;font-size:13.5px">vehicula ipsum sagittis vitae</p>
<p class="abs welcome-text">Lorem ipsum dolor sit amet, consectetur adipiscing elit. Phasellus molestie lorem vitae velit consectetur malesuada. Phasellus velit maurisco mmodo at tincidunt et, dapibus ullamcorper sapien. Donec rhoncus congue congue. Aliquam in lorem sagittis, rutrum libero sit amet, tempus lacus. Cum sociis natoque penatibus et magnis dis parturient montes,</p>

<div class="abs stat-card"></div>
<svg class="abs" style="left:100px;top:1035px" width="70" height="70" viewBox="0 0 70 70"><path d="M10 35a25 25 0 0 1 44-16M60 35a25 25 0 0 1-44 16" fill="none" stroke="#fff" stroke-width="4"/><path d="M54 8v12H42M16 62V50h12" fill="none" stroke="#fff" stroke-width="4"/><circle cx="35" cy="29" r="7" fill="#fff"/><path d="M22 48a13 11 0 0 1 26 0z" fill="#fff"/></svg>
<div class="abs" style="left:208px;top:1037px;color:#fff;font-size:20px;font-style:italic;font-weight:600">Review Score</div>
<div class="abs stars" style="left:208px;top:1072px">
  <svg width="100" height="20" viewBox="0 0 100 20"><g fill="#1d1d1d"><path id="s" d="M10 1l2.6 6 6.4.5-4.9 4.2 1.5 6.3L10 14.7 4.4 18l1.5-6.3L1 7.5l6.4-.5z"/><use href="#s" x="20"/><use href="#s" x="40"/><use href="#s" x="60"/></g><path d="M90 1l2.6 6 6.4.5-4.9 4.2 1.5 6.3L90 14.7z" fill="#888"/><path d="M90 1L87.4 7 81 7.5l4.9 4.2-1.5 6.3 5.6-3.3z" fill="#1d1d1d"/></svg>
</div>

<div class="abs divider" style="left:439px;top:1013px"></div>
<svg class="abs" style="left:486px;top:1030px" width="74" height="74" viewBox="0 0 74 74"><circle cx="37" cy="37" r="32" fill="none" stroke="#2f5b22" stroke-width="4"/><path d="M22 38l11 11 22-24" fill="none" stroke="#2f5b22" stroke-width="5"/></svg>
<div class="abs stat-title" style="left:591px;top:1037px">Reliability</div>
<div class="abs" style="left:591px;top:1072px">
  <svg width="100" height="20" viewBox="0 0 100 20"><g fill="#2a6fd6"><path id="s2" d="M10 1l2.6 6 6.4.5-4.9 4.2 1.5 6.3L10 14.7 4.4 18l1.5-6.3L1 7.5l6.4-.5z"/><use href="#s2" x="20"/><use href="#s2" x="40"/><use href="#s2" x="60"/></g><path d="M90 1l2.6 6 6.4.5-4.9 4.2 1.5 6.3L90 14.7z" fill="#aaa"/><path d="M90 1L87.4 7 81 7.5l4.9 4.2-1.5 6.3 5.6-3.3z" fill="#2a6fd6"/></svg>
</div>

<div class="abs divider" style="left:788px;top:1013px"></div>
<svg class="abs" style="left:826px;top:1030px" width="74" height="74" viewBox="0 0 74 74"><path d="M63 30A28 28 0 1 1 50 12" fill="none" stroke="#2f5b22" stroke-width="4"/><path d="M44 6l8 6-7 8" fill="none" stroke="#2f5b22" stroke-width="4"/><path d="M37 20v18l11 7" fill="none" stroke="#2f5b22" stroke-width="4"/></svg>
<div class="abs stat-title" style="left:962px;top:1037px">Punctuality</div>
<div class="abs" style="left:962px;top:1072px">
  <svg width="100" height="20" viewBox="0 0 100 20"><g fill="#2a6fd6"><path id="s3" d="M10 1l2.6 6 6.4.5-4.9 4.2 1.5 6.3L10 14.7 4.4 18l1.5-6.3L1 7.5l6.4-.5z"/><use href="#s3" x="20"/><use href="#s3" x="40"/><use href="#s3" x="60"/></g><path d="M90 1l2.6 6 6.4.5-4.9 4.2 1.5 6.3L90 14.7z" fill="#aaa"/><path d="M90 1L87.4 7 81 7.5l4.9 4.2-1.5 6.3 5.6-3.3z" fill="#2a6fd6"/></svg>
</div>

<!-- subjects & signup -->
<div class="abs subjects" role="img" aria-label="Dimmed photo of a library bookshelf behind the subjects table"></div>
<div class="abs signup"></div>
<h2 class="abs heading" style="left:84px;top:1297px;color:var(--yellow)"><span style="color:var(--white)">The</span> Subjects Taught</h2>
<div class="abs heading-rule" style="left:387px;top:1325px"></div>
<p class="abs subhead" style="left:84px;top:1335px;color:var(--white)">Vehicula Ipsum sagittis vitae</p>
<div class="abs table">
  <div class="row head"><span style="left:0">SUBJECTS TAUGHT</span><span style="left:178px">PRIMARY</span><span style="left:287px">GCSE</span><span style="left:370px">A-LEVEL</span></div>
  <div class="row"><span style="left:12px">Biology</span><span style="left:178px">£20</span><span style="left:287px">£25</span><span style="left:370px">£30</span></div>
  <div class="row"><span style="left:12px">Chemistry</span><span style="left:178px">£20</span><span style="left:287px">£25</span><span style="left:370px">£30</span></div>
</div>
<svg class="abs" style="left:84px;top:1533px" width="28" height="18" viewBox="0 0 28 18"><path d="M2 6h16l-3-4h4l7 7-7 7h-4l3-4H2z" fill="#fb6a45"/></svg>
<p class="abs note"><span style="padding-left:36px"></span>Phasellus molestie lorem vitae velit consectetur malesu da. Phasellus velit mauris, commodo at tincidunt et, dapibus ulla mcorper sapien.</p>

<h2 class="abs heading" style="left:717px;top:1297px;color:var(--yellow)"><span style="color:var(--white)">Sign</span> Up Now</h2>
<div class="abs heading-rule" style="left:910px;top:1325px"></div>
<p class="abs subhead" style="left:717px;top:1335px;color:var(--white)">Vivamus porta neque</p>
<div class="abs field" style="top:1379px">Your Name</div>
<div class="abs field" style="top:1430px">Email</div>
<div class="abs field" style="top:1481px">Phone No.</div>
<div class="abs btn btn-quote">GET FREE QUOTE</div>

<!-- featured courses -->
<h2 class="abs heading" style="left:84px;top:1773px"><span class="lead">Our</span> Featured Coures</h2>
<div class="abs heading-rule" style="left:385px;top:1801px"></div>
<p class="abs subhead" style="left:84px;top:1811px">vehicula ipsum sagittis vitae</p>

<div class="abs course-img" style="left:84px;background:linear-gradient(135deg,#6f86a8,#45618d)" role="img" aria-label="Photo of children studying together at a table"></div>
<svg class="abs" style="left:185px;top:1940px" width="40" height="40" viewBox="0 0 40 40"><path d="M20 0v40M0 20h40" stroke="#fff" stroke-width="3"/></svg>
<div class="abs course-img" style="left:346px;background:linear-gradient(135deg,#c79a6d,#6e4a30)" role="img" aria-label="Photo of a smiling student using a tablet"></div>
<div class="abs course-img" style="left:611px;background:linear-gradient(135deg,#d6d8dc,#8c96a3)" role="img" aria-label="Photo of a tutor and student working on a laptop"></div>
<div class="abs course-img" style="left:874px;background:linear-gradient(135deg,#c9a06c,#7b5634)" role="img" aria-label="Photo of a teacher with pupils in a classroom"></div>

<div class="abs course-title" style="left:84px">Vivamus Porta Neque</div>
<div class="abs course-title" style="left:346px">Vivamus Porta Neque</div>
<div class="abs course-title" style="left:611px">Vivamus Porta Neque</div>
<div class="abs course-title" style="left:874px">Vivamus Porta Neque</div>
<div class="abs course-meta" style="left:84px"><span style="color:#f7b51c">&#9679;</span>215 <span style="color:#f7b51c">&#9679;</span>08<span class="price">$399</span></div>
<div class="abs course-meta" style="left:346px"><span style="color:#f7b51c">&#9679;</span>215 <span style="color:#f7b51c">&#9679;</span>08<span class="price">$399</span></div>
<div class="abs course-meta" style="left:611px"><span style="color:#f7b51c">&#9679;</span>215 <span style="color:#f7b51c">&#9679;</span>08<span class="price">$399</span></div>
<div class="abs course-meta" style="left:874px"><span style="color:#f7b51c">&#9679;</span>215 <span style="color:#f7b51c">&#9679;</span>08<span class="price">$399</span></div>

<!-- counters -->
<div class="abs counters"></div>
<div class="abs count" style="left:84px">13</div>
<div class="abs count-label" style="left:205px">Years of<br>Experiences</div>
<div class="abs count" style="left:362px">39</div>
<div class="abs count-label" style="left:488px">Professional<br>Teacher</div>
<div class="abs count" style="left:614px">41</div>
<div class="abs count-label" style="left:741px">News Courses<br>Every Years</div>
<div class="abs count" style="left:900px">97</div>
<div class="abs count-label" style="left:1024px">Registered<br>Students</div>

<!-- latest news -->
<h2 class="abs heading" style="left:84px;top:2460px;color:var(--navy)"><span style="color:var(--orange)">OUR</span> LATEST NEWS</h2>
<div class="abs heading-rule" style="left:344px;top:2488px"></div>
<p class="abs subhead" style="left:84px;top:2498px">vehicula ipsum sagittis vitae</p>

<div class="abs news-img" style="left:84px;width:304px;background:linear-gradient(135deg,#d8a55e,#3f7fb6)" role="img" aria-label="Photo of smiling pupils reading together"></div>
<div class="abs news-img" style="left:439px;width:304px;background:linear-gradient(135deg,#3b3f4c,#9b7a5c)" role="img" aria-label="Photo of a student writing at a desk"></div>
<div class="abs news-img" style="left:790px;width:324px;background:linear-gradient(135deg,#8a6a4c,#2f4a6b)" role="img" aria-label="Photo of students studying in a library"></div>
<div class="abs news-date" style="left:84px;top:2679px">05<br>Sep</div>
<div class="abs news-date" style="left:439px;top:2679px">012<br>Nov</div>
<div class="abs news-date" style="left:790px;top:2679px">05<br>Dec</div>

<div class="abs news-meta" style="left:84px">By: Lorem Ipsum<b>Comments: 6</b></div>
<div class="abs news-meta" style="left:439px">By: Lorem Ipsum<b>Comments: 6</b></div>
<div class="abs news-meta" style="left:790px">By: Lorem Ipsum<b>Comments: 6</b></div>
<div class="abs news-title" style="left:84px">Lorem ipsum dolor sit amet, consectetur adipiscing elit.</div>
<div class="abs news-title" style="left:439px">Lorem ipsum dolor sit amet, consectetur adipiscing elit.</div>
<div class="abs news-title" style="left:790px">Lorem ipsum dolor sit amet, consectetur adipiscing elit.</div>
<p class="abs news-text" style="left:84px">Lorem ipsum dolor sit amet, consectetuipiscing elit. Phasellus molestie lorem vitae velit coetur sapien.</p>
<p class="abs news-text" style="left:439px">Lorem ipsum dolor sit amet, consectetuipiscing elit. Phasellus molestie lorem vitae velit coetur sapien.</p>
<p class="abs news-text" style="left:790px">Lorem ipsum dolor sit amet, consectetuipiscing elit. Phasellus molestie lorem vitae velit coetur sapien.</p>

<!-- footer -->
<footer>
<div class="abs footer"></div>
<div class="abs foot-brand"><span class="mark"></span>LendYourLessons</div>
<p class="abs foot-about">Lorem ipsum dolor sit amet, consectetur adipiscing elit. Phasellus molestie lorem vitae velit consectetur male.</p>
<div class="abs social" style="left:90px"></div>
<div class="abs social" style="left:131px"></div>
<div class="abs social" style="left:172px"></div>

<div class="abs foot-head" style="left:402px">Our Courses</div>
<div class="abs foot-rule" style="left:402px"></div>
<ul class="abs foot-list" style="left:402px"><li>Faster Of Taxation</li><li>Haster of IT</li><li>Hster Of Accounting</li><li>Biology</li><li>Chemistry</li></ul>

<div class="abs foot-head" style="left:629px">Quick Links</div>
<div class="abs foot-rule" style="left:629px"></div>
<ul class="abs foot-list" style="left:629px"><li>Home</li><li>Search</li><li>Student</li><li>Tutor</li><li>About</li><li>Contact</li></ul>

<div class="abs foot-head" style="left:860px">Contact Us</div>
<div class="abs foot-rule" style="left:860px"></div>
<svg class="abs" style="left:816px;top:3072px" width="14" height="18" viewBox="0 0 14 18"><path d="M7 0a7 7 0 0 1 7 7c0 5-7 11-7 11S0 12 0 7a7 7 0 0 1 7-7z" fill="#f7b51c"/><circle cx="7" cy="7" r="2.5" fill="#1a1a1a"/></svg>
<p class="abs contact-row" style="top:3068px">Lorem ipsum dolor sit amet, consectetur adipi scing elit. Phasellus molestie loremsapien.</p>
<svg class="abs" style="left:815px;top:3123px" width="16" height="12" viewBox="0 0 16 12"><rect width="16" height="12" fill="#f7b51c"/><path d="M0 0l8 6 8-6" fill="none" stroke="#1a1a1a" stroke-width="1.4"/></svg>
<p class="abs contact-row" style="top:3119px">lorem ipsum @mailbox.test</p>
<svg class="abs" style="left:816px;top:3158px" width="14" height="14" viewBox="0 0 12 12"><path d="M2 1l2.5 0 1 3-1.5 1a7 7 0 0 0 3 3l1-1.5 3 1V10a1.5 1.5 0 0 1-1.5 1.5A9.5 9.5 0 0 1 .5 2.5 1.5 1.5 0 0 1 2 1z" fill="#f7b51c"/></svg>
<p class="abs contact-row" style="top:3155px">+XXX-XXXX-XXXX</p>

<div class="abs footer-low">© 2018 Lorem ipsum dolor</div>
</footer>

</body>
</html>
```